Conference flyer

We need a flyer for a conference for the defence industry. The attached has been updated with new information using last years flyer. We would like something new and fresh. Please note the theme of the conference is 'a global environment'.

The final design should reflect the defence industry and manufacturing.

Defence

```html
<!DOCTYPE html>
<html lang="en">
<head>
<meta charset="utf-8">
<title>Defence Trade Controls Annual Conference – Flyer Draft</title>
<link href="https://fonts.googleapis.com/css2?family=Open+Sans:wght@300;400;600;700;800&display=swap" rel="stylesheet">
<style>
:root{
  --board:#1d1d1d;
  --navy:#17275e;
  --royal:#24398f;
  --sky:#3d6cc4;
  --pale:#e6edf8;
  --ink:#222;
  --label:#2457b5;
  --rule:#9aa3b5;
  --white:#fff;
}
*{box-sizing:border-box;margin:0;padding:0}
html,body{width:955px;height:1200px;overflow:hidden;background:var(--board);font-family:'Open Sans',Arial,sans-serif;color:var(--ink)}
.board{position:relative;width:955px;height:1200px}
.board-title{position:absolute;top:12px;left:0;width:100%;text-align:center;color:var(--white);font-weight:400;font-size:36px}
.page-label{position:absolute;width:384px;text-align:center;color:var(--white);font-size:17px}
.page{position:absolute;width:384px;height:498px;background:var(--white);overflow:hidden;font-size:6.4px;line-height:1.35}
.abs{position:absolute}

/* shared header */
.page-head{position:absolute;left:0;top:0;width:100%;height:80px;background:linear-gradient(180deg,#f4f7fc 0%,#dfe7f5 70%,#c8d5ee 100%)}
.page-head::after{content:"";position:absolute;left:0;bottom:0;width:100%;height:4px;background:var(--royal)}
.head-title{position:absolute;top:14px;width:100%;text-align:center;color:var(--royal);font-weight:700;line-height:1.12}
.head-title .l1{display:block;font-size:20px}
.head-title .l2{display:block;font-size:17px;font-weight:600}

.bar{position:absolute;background:var(--navy);color:var(--white);font-weight:700;font-size:7.6px;padding:0 7px;display:flex;align-items:center}

/* page 1 */
.cover-bg{position:absolute;left:0;top:0;width:100%;height:350px;background:linear-gradient(160deg,#5b86d6 0%,#2e54b2 40%,#1b2f7c 100%)}
.cover-title{position:absolute;top:12px;width:100%;text-align:center;color:var(--white);font-weight:700;line-height:1.15}
.cover-title .l1{display:block;font-size:19px}
.cover-title .l2{display:block;font-size:17px;font-weight:600}
.cover-theme{position:absolute;left:0;top:70px;width:100%;height:24px;background:var(--navy);color:var(--white);font-weight:700;font-size:10.5px;text-align:center;line-height:24px}
.cover-globe{position:absolute;left:196px;top:128px;width:226px;height:226px;border-radius:50%;background:radial-gradient(circle at 38% 40%,#e9f2ff 0%,#8fb4ec 30%,#3d6cc4 62%,#1b2f7c 100%)}
.cover-swoosh{position:absolute;left:0;top:250px}
.cover-intro{position:absolute;left:17px;top:112px;width:180px;color:var(--white);font-weight:600;font-size:9.4px;line-height:1.38}
.cover-date{position:absolute;left:17px;top:212px;color:var(--white);font-weight:700;font-size:10px;line-height:1.45}
.speakers-head{position:absolute;left:12px;top:334px;font-weight:700;font-size:9.6px;color:var(--navy)}
.speakers{position:absolute;left:12px;top:356px;list-style:none;font-size:6.6px;line-height:16.2px}
.speakers b{font-size:8.4px;font-weight:700;color:#111}
.partners{position:absolute;left:10px;top:462px;width:364px;height:30px;display:flex;justify-content:space-between;align-items:center}
.partner{display:flex;align-items:center;gap:4px;font-weight:700;font-size:9px;color:var(--navy)}
.partner .dot{width:14px;height:14px;border-radius:50%;background:var(--sky)}

/* page 2 */
.day-col{position:absolute;top:88px;width:174px}
.day-head{height:16px;background:var(--navy);color:var(--white);font-weight:700;font-size:7.6px;line-height:16px;padding-left:6px}
.sched{list-style:none;margin-top:5px}
.sched li{display:flex;min-height:13.6px}
.sched .t{width:27px;flex:none}
.sched .sub{padding-left:27px}
.note{font-size:5.4px;margin-top:4px}
.training{position:absolute;left:0;top:354px;width:100%;height:144px;background:linear-gradient(135deg,#1c2f74 0%,#14225a 100%);color:var(--white)}
.training-title{position:absolute;left:10px;top:8px;font-weight:700;font-size:10.6px}
.training-sub{position:absolute;left:10px;height:14px;background:#2c4aa6;font-weight:700;font-size:7px;line-height:14px;padding:0 6px}
.training-row{position:absolute;left:10px;font-size:6.4px;display:flex}
.training-row b{width:60px;flex:none}

/* page 3 */
.price-table{position:absolute;left:7px;top:100px;width:370px;border-collapse:collapse;font-size:6px}
.price-table th{background:#dfe3ea;font-weight:600;height:14px;font-size:6.6px}
.price-table th small{font-size:4.4px;font-weight:400}
.price-table td{height:13px;text-align:center;border-bottom:1px solid #e4e7ee}
.price-table td:first-child{font-weight:700;text-align:right;padding-right:10px;background:#eef0f4}
.info{position:absolute;left:8px;top:180px;width:368px;list-style:none}
.info li{display:flex;margin-bottom:6.3px}
.info .k{width:118px;flex:none;font-weight:700;font-size:7.6px;color:var(--label)}
.info .v{font-size:5.9px;line-height:1.34}
.info a{color:var(--label);text-decoration:none}

/* page 4 */
.reg-bar{position:absolute;left:6px;top:78px;width:372px;height:16px;background:var(--navy);color:var(--white);font-size:7.6px;display:flex;align-items:center}
.reg-bar b{background:var(--royal);height:16px;line-height:16px;padding:0 8px}
.reg-bar span{flex:1;text-align:center}
.contact{position:absolute;top:103px;width:130px;text-align:center;font-size:6.4px}
.contact svg{display:block;margin:0 auto 2px}
.form-head{position:absolute;font-weight:700;font-size:7.4px}
.field{position:absolute;left:8px;width:180px;display:flex;font-size:6.4px;align-items:flex-end}
.field .lbl{width:50px;flex:none}
.field .line{flex:1;border-bottom:1px solid var(--rule);height:7px}
.check{display:inline-block;width:6px;height:6px;border:0.8px solid #333;margin-right:5px;vertical-align:-1px}
.opt{position:absolute;font-size:6.3px;line-height:1.35}
.opt-date{position:absolute;left:206px;color:var(--label);font-weight:600;font-size:7.4px}
</style>
</head>
<body>
<main class="board">
  <h1 class="board-title">Initial Draft</h1>

  <div class="page-label" style="left:60px;top:72px">Page 1</div>
  <div class="page-label" style="left:520px;top:72px">Page 2</div>
  <div class="page-label" style="left:60px;top:650px">Page 3</div>
  <div class="page-label" style="left:520px;top:650px">Page 4</div>

  <!-- PAGE 1: cover -->
  <section class="page" style="left:60px;top:116px">
    <div class="cover-bg"></div>
    <div class="cover-globe" role="img" aria-label="Globe with network lines, representing global trade"></div>
    <svg class="cover-swoosh" width="384" height="110" viewBox="0 0 384 110" aria-hidden="true">
      <path d="M0 60 C120 110 260 96 384 20 L384 110 L0 110 Z" fill="#fff"/>
      <path d="M0 60 C120 110 260 96 384 20" fill="none" stroke="#8fb0e6" stroke-width="2"/>
    </svg>
    <h2 class="cover-title"><span class="l1">DEFENCE TRADE CONTROLS</span><span class="l2">ANNUAL CONFERENCE</span></h2>
    <div class="cover-theme">TRADE CONTROLS IN A GLOBAL ENVIRONMENT</div>
    <p class="cover-intro">Presenting the DTC 2015 Conference Australia's annual defence industry global trade controls conference</p>
    <p class="cover-date">2 &amp; 3 June, 2015<br>Harbourline Melbourne</p>
    <h3 class="speakers-head">FEATURING PRESENTATIONS FROM:</h3>
    <ul class="speakers">
      <li><b>Helena Marsh</b> Assistant Secretary, Defence Export Licensing Branch</li>
      <li><b>Rachel Dunmore</b> Managing Director, Dunmore Trade Advisory LLC</li>
      <li><b>Graham Ellison</b> Director Compliance, Commercial and Policy Allied Materiel Sales Office</li>
      <li><b>Peter Kalogeros</b> Import/Export Compliance Manager, Southern Cross Aerosystems</li>
      <li><b>Ling Zhao</b> Global Trade Compliance Director, Meridian Microdevices</li>
      <li><b>Daniel Vorster</b> Partner, Compass Trade Compliance Strategies</li>
    </ul>
    <div class="partners">
      <div class="partner"><span class="dot"></span>Defence Network</div>
      <div class="partner">Industry Alliance</div>
      <div class="partner">Velacore</div>
      <div class="partner"><span class="dot"></span>Export Assist</div>
    </div>
  </section>

  <!-- PAGE 2: programme -->
  <section class="page" style="left:520px;top:116px">
    <header class="page-head"><h2 class="head-title"><span class="l1">DEFENCE TRADE CONTROLS</span><span class="l2">ANNUAL CONFERENCE</span></h2></header>

    <div class="day-col" style="left:9px">
      <div class="day-head">DAY 1: TUESDAY, 2 JUNE 2015</div>
      <ul class="sched">
        <li><span class="t">0830</span>Registration</li>
        <li><span class="t">0900</span>Chair's welcome &amp; opening address</li>
        <li><span class="t">0915</span>Australian Legislative Changes</li>
        <li><span class="t">0950</span>Export Control Reform - next steps</li>
        <li><span class="t">1030</span>Morning tea and networking</li>
        <li><span class="t">1100</span>Managing Multi-jurisdictional Programs</li>
        <li><span class="t">1145</span>Country Focus: Japan</li>
        <li><span class="t">1230</span>Lunch</li>
        <li><span class="t">1330</span>Export Control Reform &amp; FMS,<br>CoA management</li>
        <li><span class="t">1400</span>Country Focus: Singapore</li>
        <li><span class="t">1430</span>Customs Trusted Trader Program</li>
        <li><span class="t">1500</span>Afternoon tea and networking</li>
        <li><span class="t">1530</span>Industry Best practice panelled<br>by: Daniel Vorster</li>
        <li><span class="t">1645</span>Day one wrap up</li>
        <li><span class="t">1730</span>Reception</li>
      </ul>
      <p class="note">Note: agenda &amp; Presenters may vary without notice</p>
    </div>

    <div class="day-col" style="left:201px">
      <div class="day-head">DAY 2: WEDNESDAY, 3 JUNE 2015</div>
      <ul class="sched">
        <li><span class="t">0900</span>Chair's welcome back</li>
        <li><span class="t">0910</span>Best Practice Compliance</li>
        <li><span class="t">0950</span>Compliance Case Study</li>
        <li><span class="t">1030</span>Morning tea and networking</li>
        <li><span class="t">1100</span>Practical management of export control reform</li>
        <li><span class="t">1130</span>EAR Exceptions - the good, the bad &amp; the ugly</li>
        <li><span class="t">1200</span>Country Focus: European Union</li>
        <li><span class="t">1245</span>Lunch and networking</li>
        <li><span class="t">1345</span>Export Control - round table discussions</li>
        <li class="sub">- Dual national exemptions</li>
        <li class="sub">- Understanding 'Specially Designed'</li>
        <li class="sub">- Deminimis</li>
        <li class="sub">- Re-exports under EAR</li>
        <li class="sub">- U.S. Trade Co-operation Treaty</li>
        <li class="sub">- Securing your supply chain</li>
        <li><span class="t">1500</span>Conference Q&amp;A and wrap up</li>
        <li><span class="t">1530</span>conference close</li>
      </ul>
    </div>

    <div class="training">
      <h3 class="training-title">4 X HALF DAY PRE AND POST TRAINING SESSIONS</h3>
      <div class="training-sub" style="top:30px">PRE CONFERENCE TRAINING MODULES:</div>
      <div class="training-row" style="top:50px"><b>Monday 1 June:</b>Module 1- Export Controls for Beginners - helping beginners to make the best of the conference</div>
      <div class="training-sub" style="top:68px">POST CONFERENCE TRAINING MODULES:</div>
      <div class="training-row" style="top:88px"><b>Thursday 4 June:</b>Module 2- Practi management of export control reform</div>
      <div class="training-row" style="top:104px"><b></b>Module 3- Tips and Hints for best practice compliance</div>
      <div class="training-row" style="top:120px"><b>Friday 5 June:</b>Module 4- Making the best of Commerce exceptions</div>
    </div>
  </section>

  <!-- PAGE 3: prices & information -->
  <section class="page" style="left:60px;top:694px">
    <header class="page-head"><h2 class="head-title"><span class="l1">DEFENCE TRADE CONTROLS</span><span class="l2">ANNUAL CONFERENCE</span></h2></header>
    <div class="bar" style="left:7px;top:84px;width:370px;height:14px">CONFERENCE PRICES&nbsp;<small style="font-size:5.4px">(ALL PRICES INCLUDE GST)</small></div>
    <table class="price-table">
      <tr><th></th><th>Super Earlybird <small>(prior 01 Dec 14)</small></th><th>Earlybird <small>(prior 01 Mar 15)</small></th><th>Standard Pricing</th></tr>
      <tr><td>Conference Only</td><td>$1,095</td><td>$1,095</td><td>$1,095</td></tr>
      <tr><td>Training Module</td><td>$1,095</td><td>$1,095</td><td>$1,095</td></tr>
      <tr><td>Training Module</td><td>$1,095</td><td>$1,095</td><td>$1,095</td></tr>
    </table>
    <div class="bar" style="left:7px;top:160px;width:370px;height:14px">GENERAL INFORMATION</div>
    <ul class="info">
      <li><span class="k">Conference Venue:</span><span class="v">Harbourline Melbourne 14 Riverside Quay, Southbank, 3006<br>Ph: (03) 9000 4120</span></li>
      <li><span class="k">Registration Fee Includes:</span><span class="v">Entrance to the conference, refreshments, lunch, reception event on the first evening.</span></li>
      <li><span class="k">Dress code:</span><span class="v">Business attire.</span></li>
      <li><span class="k">Accommodation and Travel:</span><span class="v">Travel and accommodation are not included in the conference fees.<br>We do not refund airfares or hotel expenses if the event is cancelled.<br>Contact Harbourline Melbourne for competitive prices.</span></li>
      <li><span class="k">Sponsorship Opportunities:</span><span class="v">Sponsoring the Defence Trade Controls Conference 2015 is a fantastic way of raising your company's profile within this market and creating greater awareness of your brand. Join us at the Defence Trade Controls Conference to promote new and existing products and service offerings in a high profile way amongst a select group of other sponsors and exhibitors.<br><a>Contact us at events@dtcevents.example to find out more information.</a></span></li>
      <li><span class="k">Early bird prices:</span><span class="v">Early bird prices only apply to conference registrations and post conference training module registrations that have been paid in full by midnight 1of the date the earlybird closes</span></li>
      <li><span class="k">Cancellation &amp; Substitution policy:</span><span class="v">Cancellations must be advised in writing at least 30 days prior to the event. An administration fee of $250 (inc. GST) will be incurred for all cancellations. A refund will not be given within 30 days of the event. If a registered attendee is unable to attend, a replacement attendee is welcome.</span></li>
      <li><span class="k">Payment Terms:</span><span class="v">Payment must be made prior to the event or admittance will not be permitted.</span></li>
      <li><span class="k">Electronic Ticket:</span><span class="v">You will recieve an electronic ticket when you register online - tickets must be presented upon entry.</span></li>
    </ul>
  </section>

  <!-- PAGE 4: registration -->
  <section class="page" style="left:520px;top:694px">
    <header class="page-head"><h2 class="head-title"><span class="l1">DEFENCE TRADE CONTROLS</span><span class="l2">ANNUAL CONFERENCE</span></h2></header>
    <div class="reg-bar"><b>HOW TO REGISTER</b><span>Complete the registration for below and return it to us by:</span></div>

    <div class="contact" style="left:-4px">
      <svg width="20" height="20" viewBox="0 0 20 20" aria-hidden="true"><circle cx="10" cy="10" r="8.5" fill="none" stroke="#17275e" stroke-width="1.6"/><ellipse cx="10" cy="10" rx="3.6" ry="8.5" fill="none" stroke="#17275e" stroke-width="1.3"/><path d="M1.5 10h17M3 5.5h14M3 14.5h14" stroke="#17275e" stroke-width="1.2"/></svg>
      Web<br>www.tradecontrolsforum.example
    </div>
    <div class="contact" style="left:127px">
      <svg width="22" height="20" viewBox="0 0 22 20" aria-hidden="true"><path d="M2 7c0-4 18-4 18 0v2h-5V7H7v2H2z" fill="#17275e"/><rect x="4" y="10" width="14" height="9" rx="2" fill="#17275e"/><circle cx="11" cy="14.5" r="2.4" fill="#fff"/></svg>
      Phone<br>+61 7 5000 1842
    </div>
    <div class="contact" style="left:258px">
      <svg width="22" height="20" viewBox="0 0 22 20" aria-hidden="true"><rect x="6" y="1" width="10" height="8" fill="#fff" stroke="#17275e" stroke-width="1.2"/><rect x="2" y="8" width="18" height="10" rx="1.5" fill="#17275e"/><rect x="6" y="11" width="10" height="2" fill="#fff"/></svg>
      Fax<br>+61 7 5000 1843
    </div>

    <h3 class="form-head" style="left:8px;top:146px">Conference Registration:</h3>
    <div class="field" style="top:164px"><span class="lbl">Attendee #1:</span><span class="line"></span></div>
    <div class="field" style="top:182px"><span class="lbl">Attendee #2:</span><span class="line"></span></div>
    <div class="field" style="top:200px"><span class="lbl">Attendee #3:</span><span class="line"></span></div>
    <div class="field" style="top:218px"><span class="lbl">Attendee #4:</span><span class="line"></span></div>
    <div class="field" style="top:236px"><span class="lbl">Company:</span><span class="line"></span></div>
    <div class="field" style="top:254px"><span class="lbl">Address:</span><span class="line"></span></div>
    <div class="field" style="top:272px"><span class="lbl">Contact no:</span><span class="line"></span></div>
    <div class="field" style="top:290px"><span class="lbl">Email:</span><span class="line"></span></div>
    <div class="field" style="top:308px"><span class="lbl">Dietary needs:</span><span class="line"></span></div>
    <div class="opt" style="left:8px;top:328px">Payment method: (please check)</div>
    <div class="opt" style="left:8px;top:344px"><span class="check"></span>Invoice</div>
    <div class="opt" style="left:8px;top:358px"><span class="check"></span>Credit card*</div>
    <div class="opt" style="left:20px;top:370px;font-size:5.6px">Credit Type: <span class="check"></span>CardOne &nbsp; <span class="check"></span>PayLine &nbsp; <span class="check"></span>TravelCard</div>
    <div class="field" style="left:20px;width:168px;top:382px;font-size:5.6px"><span class="lbl">Card name:</span><span class="line"></span></div>
    <div class="field" style="left:20px;width:168px;top:398px;font-size:5.6px"><span class="lbl">Card number:</span><span class="line"></span></div>
    <div class="field" style="left:20px;width:168px;top:414px;font-size:5.6px"><span class="lbl">Expiry date:</span><span class="line"></span></div>
    <div class="field" style="left:20px;width:168px;top:430px;font-size:5.6px"><span class="lbl">Cardholder email:</span><span class="line"></span></div>

    <h3 class="form-head" style="left:206px;top:146px">1/2 day training module/s:</h3>
    <div class="opt-date" style="top:166px">1 June 2015</div>
    <div class="opt" style="left:206px;top:180px"><span class="check"></span>Module 1 - Trade Controls for Beginner</div>
    <div class="opt-date" style="top:196px">4 June 2015</div>
    <div class="opt" style="left:206px;top:210px"><span class="check"></span>Module 2 -Practical management of export<br>&nbsp;&nbsp;&nbsp;&nbsp;control reform</div>
    <div class="opt" style="left:206px;top:232px"><span class="check"></span>Module 2 -Practical management of export<br>&nbsp;&nbsp;&nbsp;&nbsp;control reform</div>
    <div class="opt-date" style="top:256px">5 June 2015</div>
    <div class="opt" style="left:206px;top:270px"><span class="check"></span>Module 4 - Making the best of Commerce<br>&nbsp;&nbsp;&nbsp;&nbsp;exceptions</div>
    <h3 class="form-head" style="left:206px;top:296px">Training registration:</h3>
    <div class="opt" style="left:206px;top:314px"><span class="check"></span>Attendee #1: &nbsp;&nbsp;Module 1, 2, 3, 4</div>
    <div class="opt" style="left:206px;top:328px"><span class="check"></span>Attendee #2: &nbsp;&nbsp;Module 1, 2, 3, 4</div>
    <div class="opt" style="left:206px;top:342px"><span class="check"></span>Attendee #3: &nbsp;&nbsp;Module 1, 2, 3, 4</div>
    <div class="opt" style="left:206px;top:356px"><span class="check"></span>Attendee #4: &nbsp;&nbsp;Module 1, 2, 3, 4</div>
    <div class="opt" style="left:206px;top:370px;font-size:5.6px">Please tick which module each attendee would<br>like to register for</div>
    <div class="opt" style="left:206px;top:392px;font-size:5.6px">OFFICE USE ONLY:</div>
    <div class="field" style="left:206px;width:168px;top:406px;font-size:5.6px"><span class="lbl" style="width:60px">Confirmation sent:</span><span class="line"></span></div>
    <div class="field" style="left:206px;width:168px;top:422px;font-size:5.6px"><span class="lbl" style="width:60px">Contact person:</span><span class="line"></span></div>
    <div class="field" style="left:206px;width:168px;top:438px;font-size:5.6px"><span class="lbl" style="width:60px">Invoice no:</span><span class="line"></span></div>
    <div class="field" style="left:206px;width:168px;top:454px;font-size:5.6px"><span class="lbl" style="width:60px">Paid:</span><span class="line"></span></div>
  </section>
</main>
</body>
</html>
```